RTBW Core Values

Core Values poster, A fun poster that has a light feel that clearly shows the five values.

Customer 1st, Loyalty, Education, quAlity, Respect.

If it works making the letters that spell out CLEAR jump out a little.

Industry/Entity Type

Education

```html
<!DOCTYPE html>
<html lang="en">
<head>
<meta charset="utf-8">
<title>RTBW Core Values</title>
<link rel="stylesheet" href="https://fonts.googleapis.com/css2?family=Oswald:wght@400;700&family=Josefin+Sans:wght@300&display=swap">
<style>
  :root {
    --paper: #ecebe8;
    --paper-glow: #fbfaf6;
    --warm-glow: rgba(255, 196, 140, 0.45);
    --ink: #1b1612;
    --ink-soft: #4a423b;
    --rule-pink: #d23a78;
    --rule-dark: #1b1612;
    --bar-customer: #8e1414;
    --bar-loyalty: #f6ebb6;
    --bar-education: #f26a12;
    --bar-quality: #1c92d2;
    --bar-respect: #a3127e;
  }
  html, body {
    margin: 0;
    padding: 0;
    width: 1000px;
    height: 1200px;
    overflow: hidden;
    background: #ffffff;
  }
  .poster {
    position: relative;
    width: 1000px;
    height: 1200px;
    overflow: hidden;
    background:
      radial-gradient(circle at 62% 52%, var(--paper-glow) 0%, rgba(251,250,246,0.7) 30%, rgba(251,250,246,0) 60%),
      radial-gradient(circle at 30% 30%, var(--warm-glow) 0%, rgba(255,196,140,0) 25%),
      radial-gradient(circle at 85% 75%, rgba(255,170,150,0.35) 0%, rgba(255,170,150,0) 22%),
      radial-gradient(circle at 28% 88%, rgba(255,210,150,0.5) 0%, rgba(255,210,150,0) 18%),
      linear-gradient(180deg, #e4e3e0 0%, var(--paper) 45%, #dedcd8 100%);
    font-family: "Oswald", "Arial Narrow", sans-serif;
  }
  .rule {
    position: absolute;
    top: 0;
    bottom: 0;
  }
  .rule--pink {
    left: 26px;
    width: 5px;
    background: var(--rule-pink);
  }
  .rule--dark {
    left: 176px;
    width: 3px;
    background: var(--rule-dark);
  }
  .poster-title {
    position: absolute;
    left: 40px;
    top: 1160px;
    margin: 0;
    transform-origin: left top;
    transform: rotate(-90deg);
    font-family: "Josefin Sans", "Helvetica Neue", sans-serif;
    font-weight: 300;
    font-size: 148px;
    line-height: 1;
    letter-spacing: 6px;
    color: var(--ink);
    white-space: nowrap;
  }
  .brand {
    position: absolute;
    left: 270px;
    top: 78px;
    display: flex;
    flex-direction: column;
    gap: 6px;
  }
  .brand-name {
    font-family: "Oswald", "Arial Narrow", sans-serif;
    font-weight: 700;
    font-size: 96px;
    line-height: 1;
    color: var(--ink);
    letter-spacing: 2px;
  }
  .brand-tagline {
    font-family: "Josefin Sans", "Helvetica Neue", sans-serif;
    font-weight: 300;
    font-size: 32px;
    color: var(--ink-soft);
    letter-spacing: 3px;
  }
  .values {
    position: absolute;
    left: 196px;
    right: 0;
    top: 280px;
    margin: 0;
    padding: 0;
    list-style: none;
  }
  .value {
    display: flex;
    align-items: center;
    height: 100px;
    margin-bottom: 52px;
  }
  .value-name {
    flex: none;
    font-weight: 700;
    font-size: 88px;
    line-height: 1;
    color: var(--ink);
    letter-spacing: -1px;
    text-shadow: 0 0 18px rgba(255, 200, 140, 0.35);
  }
  .value-name .key {
    color: #000000;
  }
  .value-bar {
    flex: 1;
    height: 62px;
    margin-left: 4px;
    margin-top: 8px;
  }
  .value--customer .value-bar { background: linear-gradient(90deg, rgba(142,20,20,0.6), var(--bar-customer) 30%); }
  .value--loyalty .value-bar { background: linear-gradient(90deg, rgba(246,235,182,0.6), var(--bar-loyalty) 20%); }
  .value--education .value-bar { background: var(--bar-education); }
  .value--quality .value-bar { background: var(--bar-quality); }
  .value--respect .value-bar { background: linear-gradient(90deg, #c21a94, var(--bar-respect) 40%); }
  .value--customer .value-name { font-size: 86px; }
</style>
</head>
<body>
  <main class="poster">
    <div class="rule rule--pink"></div>
    <div class="rule rule--dark"></div>

    <h1 class="poster-title">CORE VALUES</h1>

    <header class="brand">
      <span class="brand-name">RTBW</span>
      <span class="brand-tagline">Learn. Grow. Belong.</span>
    </header>

    <ul class="values">
      <li class="value value--customer">
        <span class="value-name"><span class="key">C</span>USTOMER 1ST</span>
        <span class="value-bar"></span>
      </li>
      <li class="value value--loyalty">
        <span class="value-name"><span class="key">L</span>OYALTY</span>
        <span class="value-bar"></span>
      </li>
      <li class="value value--education">
        <span class="value-name"><span class="key">E</span>DUCATION</span>
        <span class="value-bar"></span>
      </li>
      <li class="value value--quality">
        <span class="value-name">QU<span class="key">A</span>LITY</span>
        <span class="value-bar"></span>
      </li>
      <li class="value value--respect">
        <span class="value-name"><span class="key">R</span>ESPECT</span>
        <span class="value-bar"></span>
      </li>
    </ul>
  </main>
</body>
</html>
```